Q & Q Fabrications HVAC Mechanical Contractor Business Card

We need a business card for a HVAC/Plumbing Mechanical Contractor. Our website is http://www.qqfabrications-example.com. We would like to include the picture of the person on the card. Pictures of people for mock-ups can be found on our website. The blue on our logo is our primary color. We'd like this to be bold yet professional without too many colors but with some color to make sure it stands out.

Industry/Entity Type

Business

Contact Information for Business Card

Font styles to use
Sans Serif

Colors
000000

Requirements
Must have
• Our logo
• Person's picture
• Company Name
• Company Phone
• Person's email address
• Person's phone number
Nice to have
• Company Address
Should not have
• Clip art

```html
<!DOCTYPE html>
<html lang="en">
<head>
<meta charset="utf-8">
<title>Q &amp; Q Fabrications – Business Card</title>
<link href="https://fonts.googleapis.com/css2?family=Bebas+Neue&family=Oswald:wght@300;400;500&display=swap" rel="stylesheet">
<style>
  :root {
    --ink: #111111;
    --paper: #ffffff;
    --brand-blue: #2f6fc0;
    --band-light: #2a8fd6;
    --band-mid: #0f72c4;
    --band-deep: #0a5aa8;
    --photo-light: #6b6b6b;
    --photo-dark: #3a3a3a;
  }
  * { margin: 0; padding: 0; box-sizing: border-box; }
  html, body { width: 667px; height: 1200px; overflow: hidden; background: var(--paper); }
  .card {
    position: relative;
    width: 667px;
    height: 1200px;
    overflow: hidden;
    background: var(--paper);
    font-family: "Oswald", "Arial Narrow", sans-serif;
    color: var(--ink);
  }
  .brand-mark {
    position: absolute;
    left: 145px; top: 77px;
    width: 377px; height: 206px;
    display: flex; align-items: center; justify-content: center; gap: 22px;
  }
  .brand-mark__square {
    width: 70px; height: 70px;
    background: var(--brand-blue);
  }
  .brand-mark__name {
    font-family: "Bebas Neue", "Oswald", sans-serif;
    font-weight: 400;
    font-size: 110px;
    line-height: 1;
    color: var(--ink);
    letter-spacing: 2px;
  }
  .company, .person {
    position: absolute; left: 0; right: 0;
    text-align: center; text-transform: uppercase;
    font-family: "Bebas Neue", "Oswald", sans-serif;
    font-weight: 400;
    line-height: 1;
    white-space: nowrap;
  }
  .company__name { top: 302px; font-size: 52px; }
  .company__trade { top: 364px; font-size: 40px; }
  .feature-band {
    position: absolute; left: 0; top: 449px;
    width: 667px; height: 423px;
    background:
      linear-gradient(115deg, transparent 0 30%, rgba(255,255,255,0.08) 30% 45%, transparent 45%),
      linear-gradient(140deg, var(--band-light) 0%, var(--band-mid) 45%, var(--band-deep) 100%);
  }
  .portrait {
    position: absolute; left: 224px; top: 482px;
    width: 219px; height: 223px;
    background: var(--paper);
    padding: 9px;
  }
  .portrait__fill {
    width: 100%; height: 100%;
    background: radial-gradient(circle at 50% 40%, var(--photo-light), var(--photo-dark));
  }
  .person { color: var(--paper); }
  .person__name { top: 724px; font-size: 64px; }
  .person__role { top: 796px; font-size: 44px; }
  .contact-item {
    position: absolute;
    display: flex; align-items: center; gap: 10px;
    font-size: 23px; font-weight: 300; color: var(--ink);
    line-height: 1;
    white-space: nowrap;
  }
  .contact-item svg { width: 28px; height: 28px; flex: none; }
</style>
</head>
<body>
<main class="card">
  <div class="brand-mark">
    <span class="brand-mark__square"></span>
    <span class="brand-mark__name">Q &amp; Q</span>
  </div>
  <h1 class="company company__name">Q &amp; Q Fabrications, Inc</h1>
  <p class="company company__trade">Mechanical Contractor</p>

  <div class="feature-band"></div>
  <div class="portrait">
    <div class="portrait__fill" role="img" aria-label="Portrait photo of Daniel Varga"></div>
  </div>
  <h2 class="person person__name">Daniel Varga</h2>
  <p class="person person__role">CEO / Project Manager</p>

  <div class="contact-item" style="left:30px; top:1006px;">
    <svg viewBox="0 0 28 28"><circle cx="14" cy="14" r="12.5" fill="none" stroke="#111" stroke-width="1.5"/><path d="M14 6.5a5 5 0 0 0-5 5c0 4 5 10 5 10s5-6 5-10a5 5 0 0 0-5-5z" fill="#111"/><circle cx="14" cy="11.5" r="1.8" fill="#fff"/></svg>
    <span>1470 Birch Road, Lakeview, WI 53000-0100</span>
  </div>
  <div class="contact-item" style="left:30px; top:1056px;">
    <svg viewBox="0 0 28 28"><circle cx="14" cy="14" r="12.5" fill="none" stroke="#111" stroke-width="1.5"/><rect x="8" y="10" width="12" height="8" fill="#111"/><path d="M8 10l6 5 6-5" fill="none" stroke="#fff" stroke-width="1.2"/></svg>
    <span>dvarga@qqfabrications-example.com</span>
  </div>
  <div class="contact-item" style="left:30px; top:1106px;">
    <svg viewBox="0 0 28 28"><circle cx="14" cy="14" r="12.5" fill="none" stroke="#111" stroke-width="1.5"/><circle cx="14" cy="14" r="7" fill="none" stroke="#111" stroke-width="1.5"/><path d="M7 14h14M14 7c-3 3-3 11 0 14M14 7c3 3 3 11 0 14" fill="none" stroke="#111" stroke-width="1.2"/></svg>
    <span>www.qqfabrications-example.com</span>
  </div>

  <div class="contact-item" style="left:449px; top:1006px;">
    <svg viewBox="0 0 28 28"><circle cx="14" cy="14" r="12.5" fill="none" stroke="#111" stroke-width="1.5"/><path d="M9.5 7.5l3 .2 1 3.3-1.8 1.3a9 9 0 0 0 4 4l1.3-1.8 3.3 1 .2 3c-1 1-2.5 1.5-4 1-4-1.5-7-4.5-8.5-8.5-.5-1.5 0-3 1.5-3.5z" fill="#111"/></svg>
    <span>+1-555-014-7720</span>
  </div>
  <div class="contact-item" style="left:449px; top:1056px;">
    <svg viewBox="0 0 28 28"><circle cx="14" cy="14" r="12.5" fill="none" stroke="#111" stroke-width="1.5"/><rect x="9.5" y="6.5" width="9" height="15" rx="1.5" fill="none" stroke="#111" stroke-width="1.5"/><circle cx="14" cy="19" r="0.9" fill="#111"/></svg>
    <span>+1-555-014-7720</span>
  </div>
  <div class="contact-item" style="left:449px; top:1106px;">
    <svg viewBox="0 0 28 28"><circle cx="14" cy="14" r="12.5" fill="none" stroke="#111" stroke-width="1.5"/><rect x="10" y="7" width="8" height="5" fill="#111"/><rect x="7" y="11" width="14" height="7" rx="1" fill="#111"/><rect x="10" y="16" width="8" height="5" fill="#fff" stroke="#111" stroke-width="1.2"/></svg>
    <span>+1-555-014-7720</span>
  </div>
</main>
</body>
</html>
```